Name should be The MORVANE. Please use logo and number 555 284 3170. Also should state "NOW LEASING".
Colors:
Witching hour (2120-30) HEX color #46494F
White Dove (OC-17) HEX color: #EFEEE5
Wilmington Tan (HC-34) HEX color: #CCB084
Oxford Gray (2128-40) HEX Color: #8290A0
Black

Target Market(s)

Renters

Industry/Entity Type

luxury rentals

Font styles to use
Serif

Colors
0054AA
0677BA
7BADD7
CADEEF
E8F1F8

Requirements
Must have
• Solid Colors and leasing information
Nice to have
• modern design, pattern
Should not have
• bright colors, bold text,

```html
<!DOCTYPE html>
<html lang="en">
<head>
<meta charset="utf-8">
<title>The MORVANE — Now Leasing Banners</title>
<link rel="stylesheet" href="https://fonts.googleapis.com/css2?family=Playfair+Display:wght@400&family=Montserrat:wght@300&display=swap">
<style>
  :root {
    --slate: #46494F;
    --ivory: #EFEEE5;
    --amber: #E9A13B;
    --ink: #000000;
    --paper: #FFFFFF;
  }
  html, body {
    margin: 0;
    padding: 0;
    width: 1000px;
    height: 1200px;
    overflow: hidden;
    background: var(--paper);
  }
  .canvas {
    position: relative;
    width: 1000px;
    height: 1200px;
  }
  .banner {
    position: absolute;
    top: 65px;
    width: 292px;
    height: 1070px;
    background: var(--slate);
  }
  .banner--leasing { left: 179px; }
  .banner--phone { left: 529px; }

  .brand {
    position: absolute;
    top: 70px;
    left: 0;
    width: 100%;
    text-align: center;
    font-family: "Playfair Display", Georgia, serif;
    font-weight: 400;
    font-size: 35px;
    line-height: 1;
    letter-spacing: 0.5px;
    color: var(--ivory);
  }
  .rule {
    position: absolute;
    left: 43px;
    width: 205px;
    height: 4px;
    background: var(--amber);
  }
  .rule--brand { top: 152px; }
  .rule--footer { top: 968px; }

  .vertical-copy {
    position: absolute;
    top: 0;
    left: 0;
    width: 292px;
    height: 997px;
  }
  .vertical-copy text {
    font-family: "Playfair Display", Georgia, serif;
    font-weight: 400;
    font-variant-numeric: lining-nums;
    font-feature-settings: "lnum" 1;
    fill: var(--ivory);
  }

  .web-band {
    position: absolute;
    left: 0;
    bottom: 0;
    width: 100%;
    height: 73px;
    background: var(--ink);
    display: flex;
    align-items: center;
    justify-content: center;
    font-family: "Montserrat", Arial, sans-serif;
    font-weight: 300;
    font-size: 22px;
    letter-spacing: 0.5px;
    color: var(--ivory);
  }
</style>
</head>
<body>
<div class="canvas">

  <section class="banner banner--leasing">
    <div class="brand">The MORVANE</div>
    <div class="rule rule--brand"></div>
    <svg class="vertical-copy" viewBox="0 0 292 997" aria-label="Now Leasing">
      <text transform="translate(183 576) rotate(-90)" text-anchor="middle"
            font-size="104" textLength="757" lengthAdjust="spacingAndGlyphs">NOW LEASING</text>
    </svg>
    <div class="web-band">MORVANELIVING.COM</div>
  </section>

  <section class="banner banner--phone">
    <div class="brand">The MORVANE</div>
    <div class="rule rule--brand"></div>
    <svg class="vertical-copy" viewBox="0 0 292 997" aria-label="555.284.3170">
      <text transform="translate(186 563) rotate(-90)" text-anchor="middle"
            font-size="108" textLength="695" lengthAdjust="spacingAndGlyphs">555.284.3170</text>
    </svg>
    <div class="rule rule--footer"></div>
    <div class="web-band">MORVANELIVING.COM</div>
  </section>

</div>
</body>
</html>
```